Business Card for Managing Partner Investment Fund

To create a business card template for an investment fund manager. Business card should be more professional in nature, not too colorful, more upscale, and created using the attached logos and fund name files. I would prefer a black or gray color scheme, but am open to the use of color as well. I would prefer a double sided business card, but open to single sided business card designs as well. The business card should include: name, title, and contact information, as well as logo and company name. I would prefer a more stream-lined, simple business card design.
Updates
Address: 4190 NE 38th Ter. Ocala, FL 34470
Email: talvin47@quorimail.net
Phone: 561-347-9162
Title: managing partner
Name: Dorian Velsky
Fund Name: Ambergate Capital
Logos can be found in files attached to the brief
Target Market(s)
potential investors, other fund managers
Industry/Entity Type
Finance
Contact Information for Business Card
Name on card: Dorian Velsky
Title: Managing Partner
Colors
Designer to choose colors to be used in the design.
Requirements
Must have
- Phone number
- email address
- physical address
- title
- name
- logo
- Fund name
Nice to have
- simple layout
Should not have
- too many colors, busy fonts,

```html
<!DOCTYPE html>
<html lang="en">
<head>
<meta charset="utf-8">
<title>Ambergate Capital – Business Card</title>
<link rel="stylesheet" href="https://fonts.googleapis.com/css2?family=Cinzel:wght@400;600&display=swap">
<style>
  :root {
    --page-bg: #e9e6e1;
    --ink-dark: #1f1d1e;
    --ink-mid: #3a3838;
    --band-grey: #8a8a8a;
    --paper: #f7f7f7;
    --paper-shade: #e4e4e4;
    --text-light: #f4f4f4;
    --text-dark: #2b2a2a;
    --text-soft: #6c6b6b;
  }
  * { box-sizing: border-box; margin: 0; padding: 0; }
  html, body { width: 1077px; height: 1200px; overflow: hidden; }
  body {
    background: var(--page-bg);
    font-family: "Cinzel", "Times New Roman", serif;
    display: flex;
    flex-direction: column;
    align-items: center;
    justify-content: center;
    gap: 60px;
  }
  .card {
    position: relative;
    width: 900px;
    height: 514px;
    overflow: hidden;
    box-shadow: 0 10px 28px rgba(0,0,0,0.25);
  }

  /* Front */
  .card--front {
    background: linear-gradient(135deg, var(--ink-mid) 0%, var(--ink-dark) 55%, #121112 100%);
  }
  .card--front .edge-band {
    position: absolute;
    top: 0; bottom: 0;
    right: 46px;
    width: 40px;
    background: var(--band-grey);
  }
  .card--front .brand {
    position: absolute;
    left: 0; right: 86px; top: 0; bottom: 0;
    display: flex;
    flex-direction: column;
    align-items: center;
    justify-content: center;
    color: var(--text-light);
    font-weight: 400;
    text-align: center;
  }
  .brand__mark {
    width: 26px; height: 26px;
    border: 2px solid currentColor;
    margin-bottom: 26px;
  }
  .brand__name {
    font-size: 66px;
    letter-spacing: 4px;
    line-height: 1;
  }
  .brand__sub {
    font-size: 34px;
    letter-spacing: 14px;
    margin-top: 12px;
    line-height: 1;
  }

  /* Back */
  .card--back {
    background: linear-gradient(160deg, #ffffff 0%, var(--paper) 50%, var(--paper-shade) 100%);
    color: var(--text-dark);
  }
  .card--back .center-band {
    position: absolute;
    top: 0; bottom: 0;
    left: 318px;
    width: 62px;
    background: linear-gradient(90deg, #2a2828, var(--ink-dark));
  }
  .card--back .brand {
    position: absolute;
    left: 0; width: 318px; top: 0; bottom: 0;
    display: flex;
    flex-direction: column;
    align-items: center;
    justify-content: center;
    color: var(--text-dark);
    font-weight: 400;
    text-align: center;
  }
  .card--back .brand__mark { width: 16px; height: 16px; margin-bottom: 16px; }
  .card--back .brand__name { font-size: 30px; letter-spacing: 2px; }
  .card--back .brand__sub { font-size: 16px; letter-spacing: 7px; margin-top: 6px; }

  .person {
    position: absolute;
    right: 56px;
    top: 62px;
    text-align: right;
  }
  .person__name {
    font-size: 40px;
    font-weight: 400;
    letter-spacing: 1.5px;
    line-height: 1;
  }
  .person__title {
    font-size: 15px;
    letter-spacing: 2.5px;
    color: var(--text-soft);
    margin-top: 8px;
    text-transform: uppercase;
  }

  .contact {
    position: absolute;
    left: 430px;
    bottom: 70px;
    list-style: none;
    display: flex;
    flex-direction: column;
    gap: 20px;
  }
  .contact__item {
    display: flex;
    align-items: center;
    gap: 16px;
    font-size: 19px;
    letter-spacing: 1px;
    text-transform: uppercase;
    color: var(--text-dark);
  }
  .contact__icon {
    width: 28px; height: 28px;
    background: var(--ink-mid);
    display: flex;
    align-items: center;
    justify-content: center;
    flex: none;
  }
  .contact__icon svg { width: 18px; height: 18px; }
</style>
</head>
<body>

  <section class="card card--front" aria-label="Business card front">
    <div class="brand">
      <span class="brand__mark" aria-hidden="true"></span>
      <span class="brand__name">AMBERGATE</span>
      <span class="brand__sub">CAPITAL</span>
    </div>
    <div class="edge-band"></div>
  </section>

  <section class="card card--back" aria-label="Business card back">
    <div class="brand">
      <span class="brand__mark" aria-hidden="true"></span>
      <span class="brand__name">AMBERGATE</span>
      <span class="brand__sub">CAPITAL</span>
    </div>
    <div class="center-band"></div>

    <div class="person">
      <h1 class="person__name">Dorian Velsky</h1>
      <p class="person__title">Managing Partner</p>
    </div>

    <ul class="contact">
      <li class="contact__item">
        <span class="contact__icon">
          <svg viewBox="0 0 24 24" fill="none" stroke="#fff" stroke-width="2" aria-hidden="true">
            <path d="M12 22s7-7.2 7-12.5A7 7 0 0 0 5 9.5C5 14.8 12 22 12 22z"/>
            <circle cx="12" cy="9.5" r="2.5"/>
          </svg>
        </span>
        4190 NE 38th Ter. Ocala, FL 34470
      </li>
      <li class="contact__item">
        <span class="contact__icon">
          <svg viewBox="0 0 24 24" fill="none" stroke="#fff" stroke-width="2" aria-hidden="true">
            <rect x="7" y="2.5" width="10" height="19" rx="1.5"/>
            <line x1="11" y1="18" x2="13" y2="18"/>
          </svg>
        </span>
        561-347-9162
      </li>
      <li class="contact__item">
        <span class="contact__icon">
          <svg viewBox="0 0 24 24" fill="none" stroke="#fff" stroke-width="2" stroke-linejoin="round" aria-hidden="true">
            <path d="M21 3 3 10.5l7 3 3 7.5z"/>
            <line x1="10" y1="13.5" x2="21" y2="3"/>
          </svg>
        </span>
        talvin47@quorimail.net
      </li>
    </ul>
  </section>

</body>
</html>
```